Al Qarmesh our website www.qrnolu.com

We need a Web Design for a new company called 'QRNOLU'. We develop innovative iPhone applications for consumers. Our initial product is PurseMeter - an application that helps people manage their budgets and save money. We would like to see designs that use the color green. The final design should communicate financial safety and growth”.

Target Market(s)

technology and Electrics

Number of Pages Required

1 page

Requirements
Must have
• And work for apple and android
• To working min 2 languages Arabic and English
Nice to have
Should not have

```html
<!DOCTYPE html>
<html lang="en">
<head>
<meta charset="utf-8">
<title>QRNOLU</title>
<link href="https://fonts.googleapis.com/css2?family=Lato:ital,wght@0,400;0,700;0,900;1,400&display=swap" rel="stylesheet">
<style>
:root{
  --green:#5aab23;
  --green-dark:#4a931a;
  --navy:#1b2148;
  --ink:#222;
  --text:#444;
  --muted:#666;
  --light:#eeeeee;
  --line:#dcdcdc;
  --white:#fff;
}
*{box-sizing:border-box;margin:0;padding:0}
html,body{width:1200px;height:3593px;overflow:hidden}
body{font-family:'Lato',sans-serif;color:var(--ink);background:var(--white);position:relative}
.abs{position:absolute}
.btn{position:absolute;background:var(--green);color:var(--white);font-weight:700;display:flex;align-items:center;justify-content:center}
.logo{display:flex;align-items:center;gap:10px;font-weight:900;font-size:34px;letter-spacing:3px;color:var(--ink)}
.logo .dot{width:18px;height:18px;border-radius:50%;background:var(--green)}
/* header */
.site-header{position:absolute;left:0;top:0;width:1200px;height:105px}
.site-header .logo{position:absolute;left:77px;top:30px}
.nav{position:absolute;left:432px;top:44px;display:flex;gap:48px;font-size:13px;font-weight:700;color:var(--ink)}
.cart{position:absolute;left:1040px;top:42px;display:flex;align-items:center;gap:6px;font-size:13px;font-weight:700;color:var(--green)}
.cart .count{width:18px;height:18px;border-radius:50%;background:var(--green);color:#fff;font-size:11px;display:flex;align-items:center;justify-content:center}
/* hero */
.hero{position:absolute;left:0;top:105px;width:1200px;height:556px;background:linear-gradient(90deg,#1a2245,#232a55 60%,#1b2046)}
.hero .art{position:absolute;left:96px;top:60px;width:455px;height:385px;background:radial-gradient(circle at 50% 50%,#3a6b9a,#26406a 55%,transparent 75%);border-radius:20px}
.hero h1{position:absolute;right:130px;top:145px;text-align:right;color:#fff;font-size:54px;font-weight:900;line-height:62px}
.hero h1 span{color:var(--green)}
.hero p{position:absolute;right:130px;top:265px;text-align:right;color:#fff;font-size:20px;font-weight:700;line-height:28px}
.hero .btn{left:893px;top:338px;width:173px;height:57px;font-size:22px}
.arrow{position:absolute}
/* about */
.about .art{position:absolute;left:120px;top:706px;width:420px;height:360px;background:radial-gradient(ellipse at 55% 45%,#c9d8ef,#e8eef8 60%,#fff 80%)}
.about h2{position:absolute;left:615px;top:728px;font-size:31px;font-weight:700}
.about h2 span{color:var(--green)}
.about p{position:absolute;left:615px;top:788px;width:500px;font-size:14.5px;line-height:25.3px;color:var(--text)}
.about .btn{left:615px;top:996px;width:182px;height:44px;font-size:16px}
/* what we do */
.what-do{position:absolute;left:0;top:1116px;width:1200px;height:498px;background:var(--green)}
.what-do .photo{position:absolute;left:599px;top:0;width:601px;height:498px;background:linear-gradient(135deg,#3b3530,#6d5e52 40%,#2c3b52 75%,#1a2233)}
.what-do .card{position:absolute;left:165px;top:98px;width:513px;height:302px;background:#fff;text-align:center;padding:50px 40px}
.what-do h2{font-size:29px;font-weight:700;margin-bottom:20px}
.what-do p{font-size:14px;line-height:23px;color:var(--text);margin-bottom:12px}
/* products */
.section-title{position:absolute;left:0;width:1200px;text-align:center;font-size:29px;font-weight:700}
.product{position:absolute;top:1741px;width:240px;height:374px;border:2px solid var(--line);background:#fff;text-align:center}
.product .shot{position:absolute;left:63px;top:22px;width:114px;height:206px;border-radius:10px;background:linear-gradient(180deg,#e9edf5,#bfd2e6)}
.product .name{position:absolute;left:0;width:100%;top:248px;font-size:19px;font-weight:700}
.product .price{position:absolute;left:0;width:100%;top:277px;font-size:18px;color:var(--text)}
.product .btn{left:55px;top:317px;width:129px;height:32px;font-size:13px}
/* offer */
.offer{position:absolute;left:0;top:2172px;width:1200px;height:261px;background:var(--light)}
.offer h2{position:absolute;left:77px;top:68px;font-size:29px;font-weight:700}
.offer .lead{position:absolute;left:77px;top:112px;width:420px;font-size:13.5px;line-height:23px;color:var(--text)}
.offer-card{position:absolute;top:34px;width:293px;height:189px;background:#fff;text-align:center}
.offer-card svg{position:absolute;left:126px;top:30px}
.offer-card h3{position:absolute;left:0;width:100%;top:94px;color:var(--green);font-size:20px;font-weight:700}
.offer-card p{position:absolute;left:30px;width:233px;top:124px;font-size:13.5px;line-height:22px;color:var(--text)}
/* blog */
.post{position:absolute;top:2548px;width:328px;height:357px;background:var(--light);text-align:center}
.post .img{width:328px;height:206px}
.post h3{margin-top:20px;color:var(--green);font-size:18px;font-weight:700}
.post p{margin:6px auto 0;width:230px;font-size:14px;line-height:23px;color:var(--text)}
.post .date{font-size:14px;font-weight:700;color:var(--ink);margin-top:2px}
/* testimonials */
.testimonials{position:absolute;left:0;top:2960px;width:1200px;height:345px;background:var(--green);color:#fff}
.testimonials h2{position:absolute;left:0;width:100%;top:50px;text-align:center;font-size:31px;font-weight:700}
.testimonials .avatar{position:absolute;left:256px;top:124px;width:164px;height:164px;border-radius:50%;background:radial-gradient(circle at 50% 40%,#b8a79a,#6c6157);border:4px solid #fff}
.testimonials blockquote{position:absolute;left:445px;top:130px;width:495px;font-style:italic;font-size:15.5px;line-height:26px}
.testimonials .who{position:absolute;left:445px;top:252px;font-size:16px;font-weight:700}
/* footer */
.site-footer .logo{position:absolute;left:77px;top:3400px;font-size:30px}
.copy{position:absolute;left:77px;top:3461px;font-size:12px;line-height:21px;color:var(--muted)}
.fcol{position:absolute;top:3355px;font-size:13px;color:var(--text)}
.fcol h4{color:var(--green);font-size:17px;font-weight:700;margin-bottom:6px}
.fcol li{list-style:none;line-height:27.8px}
.fcol .addr{line-height:23px}
.signup .field{position:absolute;left:793px;top:3403px;width:270px;height:48px;border:1px solid #bbb;font-size:13px;color:#777;display:flex;align-items:center;padding-left:16px}
.signup .go{position:absolute;left:1063px;top:3403px;width:63px;height:48px;background:var(--green);display:flex;align-items:center;justify-content:center}
.social{position:absolute;left:797px;top:3484px;display:flex;gap:20px}
.social span{width:18px;height:18px;border-radius:50%;background:#555;display:block}
</style>
</head>
<body>

<header class="site-header">
  <div class="logo"><span>QRNOLU</span><span class="dot"></span></div>
  <nav class="nav"><span>HOME</span><span>PRODUCTS</span><span>SHOP</span><span>ABOUT US</span><span>CONTACT US</span><span>BRAND</span></nav>
  <div class="cart">CART
    <svg width="18" height="16" viewBox="0 0 18 16"><path d="M0 1h3l2.5 9h9L17 3H5" fill="none" stroke="#5aab23" stroke-width="2"/><circle cx="7" cy="13.5" r="1.6" fill="#5aab23"/><circle cx="13" cy="13.5" r="1.6" fill="#5aab23"/></svg>
    <span class="count">0</span></div>
</header>

<section class="hero">
  <div class="art" role="img" aria-label="Isometric illustration of a smartphone with floating app screens"></div>
  <svg class="arrow" style="left:40px;top:258px" width="22" height="34" viewBox="0 0 22 34"><path d="M18 3L5 17l13 14" fill="none" stroke="#fff" stroke-width="4"/></svg>
  <svg class="arrow" style="left:1138px;top:258px" width="22" height="34" viewBox="0 0 22 34"><path d="M4 3l13 14L4 31" fill="none" stroke="#fff" stroke-width="4"/></svg>
  <h1>Welcome to<br><span>QRNOLU</span></h1>
  <p>Vestibulum ante ipsum primis in faucibus<br>orci luctus et ultrices posuere</p>
  <div class="btn">Read More</div>
</section>

<section class="about">
  <div class="art" role="img" aria-label="Illustration of people working around a large smartphone with charts and gears"></div>
  <h2>About <span>QRNOLU</span></h2>
  <p>Lorem ipsum dolor sit amet, consectetur adipiscing elit. Pellentesque rutrum nibh eu nibh porta molestie. Integer elit odio, tincidunt vitae tellus id, laoreet semper purus. Vivamus a tellus eu leo dictum euismod in eu sapien. Suspendisse nec libero tincidunt, aliquet dolor at, pretium erat. Morbi tincidunt erat ac purus commodo interdum. Integer euismod nec dolor ac condimentum. Donec pellentesque orci nec sagittis placerat. Nunc in odio suscipit, ullamcorper orci in, maximus nisi.</p>
  <div class="btn">Read More</div>
</section>

<section class="what-do">
  <div class="photo" role="img" aria-label="Photo of a woman testing a mobile app in front of a monitor"></div>
  <div class="card">
    <h2>What We Do</h2>
    <p>Aliquam molestie, mi et imperdiet euismod, dui purus auctor tellus, et interdum lacus lectus et ante accumsan sollicitudin sapien, sit amet adipiscing turpis gravida ac.</p>
    <p>In congue, neque ac lobortis volutpat, libero mauris varius mi, vitae suscipit ipsum ligula vitae risus.</p>
  </div>
</section>

<h2 class="section-title" style="top:1668px">Featured Products</h2>
<div class="product" style="left:77px"><div class="shot" role="img" aria-label="App screen with budget charts"></div><div class="name">Pellentesque aliquet</div><div class="price">$39.00</div><div class="btn">Add To Cart</div></div>
<div class="product" style="left:347px"><div class="shot" role="img" aria-label="App screen with bar and line graphs"></div><div class="name">Pellentesque aliquet</div><div class="price">$39.00</div><div class="btn">Add To Cart</div></div>
<div class="product" style="left:616px"><div class="shot" role="img" aria-label="Phone showing a mobile application screen"></div><div class="name">Pellentesque aliquet</div><div class="price">$39.00</div><div class="btn">Add To Cart</div></div>
<div class="product" style="left:886px"><div class="shot" role="img" aria-label="Phone showing a finance dashboard"></div><div class="name">Pellentesque aliquet</div><div class="price">$39.00</div><div class="btn">Add To Cart</div></div>

<section class="offer">
  <h2>What We Offer</h2>
  <p class="lead">Aliquam molestie, mi et imperdiet euismod, dui purus auctor tellus, et interdum lacus lectus et ante accumsan sollicitudin sapien, sit amet adipiscing turpis gravida ac.</p>
  <div class="offer-card" style="left:524px">
    <svg width="42" height="42" viewBox="0 0 42 42"><path d="M19 4A18 18 0 1 0 38 23H19Z" fill="#333"/><path d="M23 0A18 18 0 0 1 42 19H23Z" fill="#333"/></svg>
    <h3>Manage Budgets</h3><p>Aliquam molestie, mi et imperdiet euismod, dui purus auctor</p>
  </div>
  <div class="offer-card" style="left:833px">
    <svg width="42" height="46" viewBox="0 0 42 46"><text x="21" y="40" text-anchor="middle" font-family="Lato,sans-serif" font-weight="900" font-size="46" fill="#333">$</text></svg>
    <h3>Save Money</h3><p>Aliquam molestie, mi et imperdiet euismod, dui purus auctor</p>
  </div>
</section>

<h2 class="section-title" style="top:2476px">Blog Posts</h2>
<article class="post" style="left:77px"><div class="img" role="img" aria-label="Photo of a laptop showing code" style="background:linear-gradient(160deg,#5a6470,#23282f)"></div><h3>Neque porro quisquam est qui</h3><p>Morbi tincidunt erat ac purus commodo interdum erat....</p><div class="date">Jan 18, 2018</div></article>
<article class="post" style="left:436px"><div class="img" role="img" aria-label="Photo of a developer desk with monitor and phone" style="background:linear-gradient(160deg,#d8dde2,#3a3f45)"></div><h3>Neque porro quisquam est qui</h3><p>Morbi tincidunt erat ac purus commodo interdum erat....</p><div class="date">Jan 18, 2018</div></article>
<article class="post" style="left:795px"><div class="img" role="img" aria-label="Photo of a hand holding a phone with a colourful app" style="background:linear-gradient(160deg,#8a7a6a,#c9b89a 50%,#5e6b7a)"></div><h3>Neque porro quisquam est qui</h3><p>Morbi tincidunt erat ac purus commodo interdum erat....</p><div class="date">Jan 18, 2018</div></article>

<section class="testimonials">
  <h2>Testimonials</h2>
  <svg class="arrow" style="left:212px;top:196px" width="16" height="26" viewBox="0 0 16 26"><path d="M13 2L3 13l10 11" fill="none" stroke="#fff" stroke-width="3.5"/></svg>
  <svg class="arrow" style="left:972px;top:196px" width="16" height="26" viewBox="0 0 16 26"><path d="M3 2l10 11L3 24" fill="none" stroke="#fff" stroke-width="3.5"/></svg>
  <div class="avatar" role="img" aria-label="Portrait photo of the client"></div>
  <blockquote>" Lorem ipsum dolor sit amet, consectetur adipiscing elit neque odio, luctus ac libero eget, accumsan pellentesque felis. Proin ullamcorper tortor vitae sodales efficitur. Pellentesque aliquet augue eget eleifend congue. Integer non lectus mattis..."</blockquote>
  <div class="who">- Name Heading</div>
</section>

<footer class="site-footer">
  <div class="logo"><span>QRNOLU</span><span class="dot"></span></div>
  <div class="copy">Copyright © 2019 Company Name<br>All Right Reserved</div>
  <div class="fcol" style="left:354px"><h4>Site Map</h4><ul><li>Home</li><li>Products</li><li>Shop</li><li>About Us</li><li>Contact Us</li><li>Brand</li></ul></div>
  <div class="fcol" style="left:534px"><h4>Contact Info</h4><div class="addr">Harbor Lane Street<br>(North Loop Road)<br>+96770400100, +967 1000222<br>info@qrnolu.com</div></div>
  <div class="fcol signup" style="left:793px"><h4>Email Sign Up</h4></div>
  <div class="signup"><div class="field">Enter Email Address</div><div class="go"><svg width="22" height="20" viewBox="0 0 22 20"><path d="M1 10h17M11 2l8 8-8 8" fill="none" stroke="#fff" stroke-width="3.5"/></svg></div></div>
  <div class="social"><span></span><span></span><span></span><span></span><span></span></div>
</footer>

</body>
</html>
```